I need a vertical business card designed to incorporate 2 Companies in wheaton IL. First company is sol e frame (I always type this with no caps and in Cataneo BT font. I like the way the L and the P surround the i) This is a Photography company that does Wedding Photography, Portraiture, Sunset, and many other types of Photography. The website is www.solframeworks.example
The other company is Grand Kiosk Max a Photo Booth rental Company. We rent photo booths to weddings and all types of events. The end project should mainly appeal to Brides and show Class. I have added 2 files One is the Grand Kiosk Max Logo and the other is on sol E frames header on the website. I do Like the eye in the sky on the sol E frame file

Target Market(s)

Future brides

Industry/Entity Type

Business

Requirements
Must have
• Grand Kiosk Max part should say A Photo Booth Rental Company
sol e frame should say All in one photography studio and address should be on this side,

```html
<!DOCTYPE html>
<html lang="en">
<head>
<meta charset="utf-8">
<title>Grand Kiosk Max and sol e frame — Business Card</title>
<link rel="stylesheet" href="https://fonts.googleapis.com/css2?family=Montserrat:wght@400;500;700&display=swap">
<style>
  :root {
    --backdrop: #374455;
    --card-red: #c1292e;
    --card-white: #ffffff;
    --label-yellow: #fde38a;
    --label-border: #f4ce5c;
    --plum: #5a1a5e;
    --contact-yellow: #fbd877;
    --frame-white: #f7fbfa;
    --photo-pink: #f5c6d6;
    --photo-peach: #f8d9a8;
    --photo-rose: #ee9fbd;
  }
  * { margin: 0; padding: 0; box-sizing: border-box; }
  html, body {
    width: 1200px; height: 1200px; overflow: hidden;
    background: var(--backdrop);
    font-family: "Montserrat", Arial, sans-serif;
  }
  .card {
    position: absolute; left: 296px; top: 63px;
    width: 609px; height: 1073px;
    background: var(--card-red);
    overflow: hidden;
  }
  .studio-strip {
    position: absolute; left: 0; top: 0;
    width: 100%; height: 83px;
    display: flex; flex-direction: column;
    align-items: center; justify-content: center;
    color: var(--contact-yellow);
    font-size: 19px; font-weight: 400; line-height: 1.35;
    text-align: center;
  }
  .studio-strip .studio-name { font-weight: 500; }
  .brand-band {
    position: absolute; left: 0; top: 83px;
    width: 100%; height: 237px;
    background: var(--card-white);
  }
  .brand-name {
    position: absolute; left: 0; top: 62px; width: 100%;
    text-align: center;
    font-weight: 700; font-size: 58px; letter-spacing: -0.5px;
    color: var(--plum);
    white-space: nowrap;
  }
  .tagline {
    position: absolute; left: 49px; top: 291px;
    width: 510px; height: 63px;
    background: var(--label-yellow);
    border: 2px solid var(--label-border);
    display: flex; align-items: center; justify-content: center;
    font-size: 30px; font-weight: 400; color: var(--plum);
  }
  .contact {
    position: absolute; left: 74px; top: 438px;
    list-style: none;
    color: var(--contact-yellow);
    font-size: 29px; font-weight: 400; line-height: 1.4;
  }
  .contact .web { margin-top: 10px; }
  .photo-frame {
    position: absolute; left: 0; top: 0; width: 100%; height: 100%;
  }
</style>
</head>
<body>
  <div class="card">
    <div class="studio-strip">
      <p><span class="studio-name">sol e frame</span> · All in one photography studio</p>
      <p>214 Elm Row, Wheaton IL 60187</p>
    </div>
    <div class="brand-band">
      <div class="brand-name">Grand Kiosk Max</div>
    </div>
    <div class="tagline">photobooth rental company</div>
    <ul class="contact">
      <li>555 014 2290</li>
      <li>photodesk@solframe.example</li>
      <li class="web">www.grandkioskmax.example</li>
    </ul>
    <svg class="photo-frame" viewBox="0 0 609 1073">
      <defs>
        <linearGradient id="photoTone" x1="0" y1="0" x2="1" y2="1">
          <stop offset="0" stop-color="var(--photo-pink)"/>
          <stop offset="0.55" stop-color="#f6cbd8"/>
          <stop offset="0.8" stop-color="var(--photo-peach)"/>
          <stop offset="1" stop-color="var(--photo-rose)"/>
        </linearGradient>
      </defs>
      <g transform="rotate(-5 340 830)">
        <rect x="72" y="615" width="560" height="470" rx="26" fill="var(--frame-white)"/>
        <rect role="img" aria-label="Pink instant photo print decorated with soft stars" x="108" y="645" width="490" height="390" rx="22" fill="url(#photoTone)"/>
      </g>
    </svg>
  </div>
</body>
</html>
```